Brightway Inc. Business Card Design

Brightway Inc. is in search of a great clean design for our business cards!

Looking to incorporate our full logo and watermark on side one (however, I am open to having the text and watermark separated within the design.)

On side two, I am looking to have contact information (Name, Position, Phone #, Email, Website (www.thebrightway.ca). Can have the logo and/or watermark as part of the design if applicable.

Please add tagline "Where Shine Counts" on either side 1 or 2. This tagline can be in a sans serif, serif or cursive font as long as it compliments overall design. Capitalization can be title or sentence case depending on how it fits within the design.

Get creative!! Looking for a clean, crisp, premium design! Looking for a glossy card finish with spot UV features when printed. Cards will also be printed with rounded corners. Standard dimensions (3.5 x 2).

Target Market(s)

B2B - primary clients are business owners or property management corporations. (residential jobs are few and far between)

Industry/Entity Type

Business

Contact Information for Business Card

- clean, crisp design
- double sided
- spot UV accents and glossy finish upon printing
- standard business card size (3.5 x 2) with rounded corners
- please see project description for requirements per side

Font styles to use
Sans Serif

Requirements
Must have
• - adequate bleeds with print ready files
• - cohesive design elements between side 1 & 2
• - spot UV elements (can be on both sides or just one, use your discretion)
• - colour pallet should match the logo file provided
• - incorporate tagline "where shine counts" (this tagline can be in a serif or sans serif font as long as it is complimentary to the overall design.
Nice to have
• - Premium elements with a clean design
Should not have
• - Please omit cartoon or whimsical like designs, think premium.
• - Colours should not stray from the pallet of the provided logo.

```html
<!DOCTYPE html>
<html lang="en">
<head>
<meta charset="utf-8">
<title>Brightway Inc. Business Card</title>
<link rel="stylesheet" href="https://fonts.googleapis.com/css2?family=Open+Sans:wght@400;600;700;800&display=swap">
<style>
  :root {
    --backdrop: #00bfc4;
    --navy: #343f78;
    --navy-deep: #2b3468;
    --teal: #1fcbd3;
    --white: #ffffff;
    --paper: #fbfbfb;
    --ink: #2a2f66;
  }
  * { box-sizing: border-box; margin: 0; padding: 0; }
  html, body {
    width: 1200px;
    height: 1200px;
    overflow: hidden;
    background: var(--backdrop);
    font-family: "Open Sans", Arial, sans-serif;
  }
  .sheet {
    width: 1200px;
    height: 1200px;
    display: flex;
    flex-direction: column;
    align-items: center;
    justify-content: center;
    gap: 56px;
  }
  .card {
    position: relative;
    width: 900px;
    height: 514px;
    border-radius: 22px;
    overflow: hidden;
    box-shadow: 0 18px 40px rgba(0, 60, 70, 0.22);
  }
  /* Side one: contact side */
  .card--contact {
    background: radial-gradient(circle at 40% 30%, #3d4883 0%, var(--navy) 45%, var(--navy-deep) 100%);
  }
  .card__arc {
    position: absolute;
    right: -150px;
    top: 80px;
    width: 300px;
    height: 300px;
    border-radius: 50%;
    background: var(--white);
  }
  .brand-name {
    position: absolute;
    left: 70px;
    top: 62px;
    font-weight: 800;
    font-size: 70px;
    letter-spacing: -1px;
    color: var(--teal);
    line-height: 1;
  }
  .person {
    position: absolute;
    left: 70px;
    top: 168px;
  }
  .person__name {
    font-weight: 700;
    font-size: 34px;
    line-height: 1.1;
    color: var(--white);
  }
  .person__role {
    margin-top: 6px;
    font-weight: 600;
    font-size: 22px;
    letter-spacing: 1px;
    line-height: 1.1;
    text-transform: uppercase;
    color: var(--teal);
  }
  .contact-list {
    position: absolute;
    left: 70px;
    top: 290px;
    list-style: none;
    display: flex;
    flex-direction: column;
    gap: 20px;
  }
  .contact-list__item {
    display: flex;
    align-items: center;
    gap: 22px;
    color: var(--white);
    font-weight: 600;
    font-size: 30px;
    line-height: 1;
  }
  .contact-list__icon {
    width: 28px;
    height: 28px;
    flex: none;
  }
  /* Side two: brand side */
  .card--brand {
    background: var(--paper);
  }
  .brand-lockup {
    position: absolute;
    left: 0;
    right: 0;
    top: 150px;
    display: flex;
    align-items: center;
    justify-content: center;
    gap: 22px;
  }
  .brand-lockup__square {
    width: 56px;
    height: 56px;
    background: var(--teal);
  }
  .brand-lockup__name {
    font-weight: 800;
    font-size: 58px;
    letter-spacing: -1px;
    color: var(--navy);
    line-height: 1;
  }
  .tagline {
    position: absolute;
    left: 0;
    right: 0;
    top: 330px;
    text-align: center;
    font-weight: 800;
    font-size: 44px;
    letter-spacing: -1px;
    color: var(--ink);
  }
</style>
</head>
<body>
  <main class="sheet">
    <section class="card card--contact" aria-label="Business card contact side">
      <div class="card__arc"></div>
      <h1 class="brand-name">BRIGHTWAY INC.</h1>
      <div class="person">
        <p class="person__name">Jordan Ellis</p>
        <p class="person__role">Operations Manager</p>
      </div>
      <ul class="contact-list">
        <li class="contact-list__item">
          <svg class="contact-list__icon" viewBox="0 0 30 30" aria-hidden="true">
            <circle cx="15" cy="15" r="13" fill="none" stroke="#1fcbd3" stroke-width="3"/>
            <ellipse cx="15" cy="15" rx="5.5" ry="13" fill="none" stroke="#1fcbd3" stroke-width="2.5"/>
            <line x1="2" y1="15" x2="28" y2="15" stroke="#1fcbd3" stroke-width="2.5"/>
          </svg>
          <span>www.thebrightway.ca</span>
        </li>
        <li class="contact-list__item">
          <svg class="contact-list__icon" viewBox="0 0 30 30" aria-hidden="true">
            <circle cx="15" cy="15" r="5" fill="none" stroke="#1fcbd3" stroke-width="3"/>
            <path d="M20 10 V18 Q20 22 24 21 Q28 19 28 15 A13 13 0 1 0 22 26" fill="none" stroke="#1fcbd3" stroke-width="3" stroke-linecap="round"/>
          </svg>
          <span>info@brightwaycare.ca</span>
        </li>
        <li class="contact-list__item">
          <svg class="contact-list__icon" viewBox="0 0 30 30" aria-hidden="true">
            <path d="M3 9 Q15 1 27 9 L24 13 L19 11 L19 8 Q15 7 11 8 L11 11 L6 13 Z" fill="#1fcbd3"/>
            <path d="M8 14 H22 L26 27 H4 Z" fill="#1fcbd3"/>
            <circle cx="15" cy="20" r="3.5" fill="#343f78"/>
          </svg>
          <span>555-014-2290</span>
        </li>
      </ul>
    </section>

    <section class="card card--brand" aria-label="Business card brand side">
      <div class="brand-lockup">
        <div class="brand-lockup__square"></div>
        <span class="brand-lockup__name">Brightway Inc.</span>
      </div>
      <p class="tagline">where shine counts</p>
    </section>
  </main>
</body>
</html>
```